Staffing Firm - Business Cards and Stationary
Business Cards, Letterhead, Envelopes and Brochure Layout
I need double sided standard sized Business Card [3.5" x 2"]
Use whatever fonts that you think are best.
Professional
Todd Dunlap
President/CEO
2250 North Birch Avenue, Ste 730
Houston, TX 77027
Direct Line - 832-555-0143
tdunlap@kelvor.com
www.kelvor.com
We would like them to be memorable but professional.
Possibly put the various divisions?
We will need layouts for each group/division.

```html
<!DOCTYPE html>
<html lang="en">
<head>
<meta charset="utf-8">
<title>Kelvor Staffing – Stationery Set</title>
<link href="https://fonts.googleapis.com/css2?family=Libre+Baskerville:wght@400&family=Open+Sans:wght@400;600&display=swap" rel="stylesheet">
<style>
:root{
  --stage:#2b2623;
  --paper:#ffffff;
  --ink:#3a3a3a;
  --soft:#8a8a8a;
  --rule:#b9b9b9;
  --night:#111111;
  --night-2:#2c2c2c;
  --on-night:#e8e8e8;
  --on-night-soft:#9a9a9a;
  --div-credit:#2f2f2f;
  --div-search:#7a2a80;
  --div-testing:#a3262e;
  --div-tech:#2d5d9a;
}
*{box-sizing:border-box;margin:0;padding:0}
html,body{width:1200px;height:874px;overflow:hidden;background:var(--stage)}
body{position:relative;font-family:"Open Sans",Arial,sans-serif;color:var(--ink)}

/* wordmark */
.wordmark{font-family:"Libre Baskerville",Georgia,serif;letter-spacing:.08em;text-transform:uppercase;line-height:1.05;color:var(--ink);white-space:nowrap}
.wordmark .dot{display:inline-block;width:.55em;height:.55em;border-radius:50%;background:currentColor;margin-right:.35em;vertical-align:.1em}
.tagline{font-size:7px;font-weight:600;letter-spacing:.04em;white-space:nowrap}

/* business card front */
.card-front{position:absolute;left:77px;width:236px;height:132px;background:var(--paper);padding:12px 12px}
.card-front .wordmark{font-size:14px}
.card-front .tagline{margin:3px 0 0 20px}
.card-front .person{position:absolute;left:12px;top:80px;width:96px}
.card-front .person-name{font-family:"Libre Baskerville",Georgia,serif;font-size:12.5px;color:var(--ink);white-space:nowrap}
.card-front .person-title{font-family:"Libre Baskerville",Georgia,serif;font-size:7px;color:var(--soft);border-top:1px solid var(--rule);padding-top:2px;margin-top:2px;white-space:nowrap}
.card-front .contact{position:absolute;left:120px;top:62px;border-left:1px solid var(--rule);padding-left:6px;font-size:4.8px;line-height:1.55;color:var(--ink);white-space:nowrap}

/* business card back */
.card-back{position:absolute;left:324px;width:236px;height:132px;background:linear-gradient(160deg,var(--night-2),var(--night) 70%);color:var(--on-night);display:flex;flex-direction:column;align-items:center;justify-content:center}
.card-back .wordmark{font-size:15px;color:var(--on-night)}
.card-back .tagline{color:var(--on-night-soft);margin-top:3px}
.card-back .divisions{display:grid;grid-template-columns:auto auto;column-gap:10px;font-size:5px;color:var(--on-night-soft);margin-top:14px;line-height:1.5;white-space:nowrap}

/* letterhead */
.letterhead{position:absolute;top:84px;width:283px;height:372px;background:var(--paper);padding:16px 18px}
.letterhead .head{display:flex;gap:10px;align-items:flex-start}
.letterhead .wordmark{font-size:11px}
.letterhead .tagline{font-size:5.5px;margin:2px 0 0 15px}
.letterhead .head-address{font-size:4.2px;line-height:1.5;border-left:1px solid var(--rule);padding-left:5px;margin-top:2px;white-space:nowrap}
.letterhead .foot-divisions{position:absolute;left:18px;right:18px;bottom:26px;font-size:4.4px;color:var(--soft);display:flex;justify-content:space-between;white-space:nowrap}
.letterhead .foot-address{position:absolute;left:18px;right:18px;bottom:12px;font-size:4.2px;color:var(--soft);text-align:right;white-space:nowrap}

/* envelope */
.envelope-front{position:absolute;top:497px;width:283px;height:122px;background:var(--paper);padding:12px 14px}
.envelope-front .head{display:flex;gap:10px}
.envelope-front .wordmark{font-size:10px}
.envelope-front .tagline{font-size:5px;margin:2px 0 0 13px}
.envelope-front .head-address{font-size:4.2px;line-height:1.5;border-left:1px solid var(--rule);padding-left:5px;white-space:nowrap}
.envelope-back{position:absolute;top:619px;width:283px;height:174px}
.envelope-back svg{position:absolute;inset:0}
.envelope-back .flap-mark{position:absolute;left:0;right:0;top:30px;text-align:center}
.envelope-back .wordmark{font-size:10px;color:var(--on-night)}
.envelope-back .tagline{font-size:5px;color:var(--on-night-soft);margin-top:2px}
</style>
</head>
<body>

<!-- business cards: fronts -->
<section class="card-front" style="top:84px">
  <div class="wordmark"><span class="dot"></span>Kelvor<br>Staffing</div>
  <div class="tagline" style="color:var(--soft)">staffing solutions</div>
  <div class="person"><div class="person-name">Todd Dunlap</div><div class="person-title">President/CEO</div></div>
  <div class="contact">2250 North Birch Avenue, Ste 730<br>Houston, TX 77027<br>Direct 832-555-0143<br>tdunlap@kelvor.com<br>www.kelvor.com</div>
</section>
<section class="card-front" style="top:233px">
  <div class="wordmark"><span class="dot"></span>Kelvor<br>Staffing</div>
  <div class="tagline" style="color:var(--div-credit)">credit and risk group</div>
  <div class="person"><div class="person-name">Todd Dunlap</div><div class="person-title">President/CEO</div></div>
  <div class="contact">2250 North Birch Avenue, Ste 730<br>Houston, TX 77027<br>Direct 832-555-0143<br>tdunlap@kelvor.com<br>www.kelvor.com</div>
</section>
<section class="card-front" style="top:372px">
  <div class="wordmark"><span class="dot"></span>Kelvor<br>Staffing</div>
  <div class="tagline" style="color:var(--div-search)">professional search group</div>
  <div class="person"><div class="person-name">Todd Dunlap</div><div class="person-title">President/CEO</div></div>
  <div class="contact">2250 North Birch Avenue, Ste 730<br>Houston, TX 77027<br>Direct 832-555-0143<br>tdunlap@kelvor.com<br>www.kelvor.com</div>
</section>
<section class="card-front" style="top:514px">
  <div class="wordmark"><span class="dot"></span>Kelvor<br>Staffing</div>
  <div class="tagline" style="color:var(--div-testing)">testing services group</div>
  <div class="person"><div class="person-name">Todd Dunlap</div><div class="person-title">President/CEO</div></div>
  <div class="contact">2250 North Birch Avenue, Ste 730<br>Houston, TX 77027<br>Direct 832-555-0143<br>tdunlap@kelvor.com<br>www.kelvor.com</div>
</section>
<section class="card-front" style="top:653px">
  <div class="wordmark"><span class="dot"></span>Kelvor<br>Staffing</div>
  <div class="tagline" style="color:var(--div-tech)">technology services group</div>
  <div class="person"><div class="person-name">Todd Dunlap</div><div class="person-title">President/CEO</div></div>
  <div class="contact">2250 North Birch Avenue, Ste 730<br>Houston, TX 77027<br>Direct 832-555-0143<br>tdunlap@kelvor.com<br>www.kelvor.com</div>
</section>

<!-- business cards: backs -->
<section class="card-back" style="top:84px">
  <div class="wordmark"><span class="dot"></span>Kelvor Staffing</div>
  <div class="tagline">staffing solutions</div>
  <div class="divisions"><span>credit and risk group</span><span>professional search group</span><span>technology services group</span><span>testing services group</span></div>
</section>
<section class="card-back" style="top:233px">
  <div class="wordmark"><span class="dot"></span>Kelvor Staffing</div>
  <div class="tagline">staffing solutions</div>
  <div class="divisions"><span>credit and risk group</span><span>professional search group</span><span>technology services group</span><span>testing services group</span></div>
</section>
<section class="card-back" style="top:372px">
  <div class="wordmark"><span class="dot"></span>Kelvor Staffing</div>
  <div class="tagline">staffing solutions</div>
  <div class="divisions"><span>credit and risk group</span><span>professional search group</span><span>technology services group</span><span>testing services group</span></div>
</section>
<section class="card-back" style="top:514px">
  <div class="wordmark"><span class="dot"></span>Kelvor Staffing</div>
  <div class="tagline">staffing solutions</div>
  <div class="divisions"><span>credit and risk group</span><span>professional search group</span><span>technology services group</span><span>testing services group</span></div>
</section>
<section class="card-back" style="top:653px">
  <div class="wordmark"><span class="dot"></span>Kelvor Staffing</div>
  <div class="tagline">staffing solutions</div>
  <div class="divisions"><span>credit and risk group</span><span>professional search group</span><span>technology services group</span><span>testing services group</span></div>
</section>

<!-- letterheads -->
<section class="letterhead" style="left:576px">
  <div class="head">
    <div><div class="wordmark"><span class="dot"></span>Kelvor<br>Staffing</div><div class="tagline" style="color:var(--soft)">staffing solutions</div></div>
    <div class="head-address">2250 North Birch Avenue, Ste 730<br>Houston, TX 77027<br>832-555-0143<br>www.kelvor.com</div>
  </div>
  <div class="foot-divisions"><span>credit and risk group</span><span>professional search group</span><span>technology services group</span><span>testing services group</span></div>
</section>
<section class="letterhead" style="left:883px">
  <div class="head">
    <div><div class="wordmark"><span class="dot"></span>Kelvor<br>Staffing</div><div class="tagline" style="color:var(--soft)">staffing solutions</div></div>
  </div>
  <div class="foot-address">2250 North Birch Avenue, Ste 730 · Houston, TX 77027 · 832-555-0143 · www.kelvor.com</div>
</section>

<!-- envelopes: fronts -->
<section class="envelope-front" style="left:576px">
  <div class="head">
    <div><div class="wordmark"><span class="dot"></span>Kelvor<br>Staffing</div><div class="tagline" style="color:var(--soft)">staffing solutions</div></div>
    <div class="head-address">2250 North Birch Avenue, Ste 730<br>Houston, TX 77027</div>
  </div>
</section>
<section class="envelope-front" style="left:883px">
  <div class="head">
    <div><div class="wordmark"><span class="dot"></span>Kelvor<br>Staffing</div><div class="tagline" style="color:var(--soft)">staffing solutions</div></div>
    <div class="head-address">2250 North Birch Avenue, Ste 730<br>Houston, TX 77027</div>
  </div>
</section>

<!-- envelopes: backs -->
<section class="envelope-back" style="left:576px">
  <svg width="283" height="174" viewBox="0 0 283 174">
    <rect width="283" height="174" fill="#1a1a1a"/>
    <path d="M0 0H283V40L141.5 96L0 40Z" fill="#2e2e2e"/>
    <path d="M0 40L141.5 96L283 40" fill="none" stroke="#555" stroke-width="1"/>
  </svg>
  <div class="flap-mark"><div class="wordmark"><span class="dot"></span>Kelvor Staffing</div><div class="tagline">staffing solutions</div></div>
</section>
<section class="envelope-back" style="left:883px">
  <svg width="283" height="174" viewBox="0 0 283 174">
    <rect width="283" height="174" fill="#1a1a1a"/>
    <path d="M0 0H283V40L141.5 96L0 40Z" fill="#2e2e2e"/>
    <path d="M0 40L141.5 96L283 40" fill="none" stroke="#555" stroke-width="1"/>
  </svg>
  <div class="flap-mark"><div class="wordmark"><span class="dot"></span>Kelvor Staffing</div><div class="tagline">staffing solutions</div></div>
</section>

</body>
</html>
```